Design Book Cover - Win The Hiring Room

Need assistance designing a compelling cover for an eBook titled "Win The Hiring Room". eBook is a hard hitting, direct tutorial for how to succeed in a job interview. Written by Derek Pollfrey, a senior partner with 20 years interviewing people for employment at one of the largest and most prestigious consulting firms in the world.

Target Market(s)

anyone looking to land a corporate job with Summit 1000 companies

Industry/Entity Type

Consulting

```html
<!DOCTYPE html>
<html lang="en">
<head>
<meta charset="utf-8">
<title>Win The Hiring Room — Book Cover</title>
<link rel="stylesheet" href="https://fonts.googleapis.com/css2?family=Cinzel:wght@700&family=Creepster&display=swap">
<style>
  :root {
    --page-bg: #ffffff;
    --cover-dark: #0b0b0b;
    --cover-mid: #1c1c1c;
    --blood-deep: #4a0508;
    --blood-bright: #c0141b;
    --title-dark: #5a1a1f;
    --title-light: #c9a7ab;
    --title-edge: #e8cfd2;
  }
  html, body {
    margin: 0;
    padding: 0;
    width: 1200px;
    height: 1000px;
    overflow: hidden;
    background: var(--page-bg);
  }
  .cover-sheet {
    display: block;
    width: 1200px;
    height: 1000px;
  }
  .title-word {
    font-family: "Cinzel", "Times New Roman", serif;
    font-weight: 700;
    fill: url(#titleGloss);
    stroke: var(--title-edge);
    stroke-width: 1.4;
    paint-order: stroke fill;
  }
  .title-verb {
    font-family: "Creepster", "Impact", fantasy;
    font-weight: 400;
    fill: url(#bloodFill);
  }
  .title-verb--spine {
    fill: url(#bloodSpine);
  }
</style>
</head>
<body>
<svg class="cover-sheet" viewBox="0 0 1200 1000" xmlns="http://www.w3.org/2000/svg">
  <defs>
    <linearGradient id="coverFill" x1="0" y1="0" x2="1" y2="1">
      <stop offset="0" style="stop-color:var(--cover-mid)"/>
      <stop offset="1" style="stop-color:var(--cover-dark)"/>
    </linearGradient>
    <linearGradient id="spineFill" x1="0" y1="0" x2="1" y2="0">
      <stop offset="0" style="stop-color:var(--cover-mid)"/>
      <stop offset="0.5" style="stop-color:#262626"/>
      <stop offset="1" style="stop-color:var(--cover-mid)"/>
    </linearGradient>
    <linearGradient id="bloodFill" x1="0" y1="0" x2="0" y2="1">
      <stop offset="0" style="stop-color:var(--blood-bright)"/>
      <stop offset="1" style="stop-color:var(--blood-deep)"/>
    </linearGradient>
    <linearGradient id="bloodSpine" x1="0" y1="0" x2="1" y2="0">
      <stop offset="0" style="stop-color:var(--blood-deep)"/>
      <stop offset="1" style="stop-color:var(--blood-bright)"/>
    </linearGradient>
    <radialGradient id="splatterFill" cx="0.5" cy="0.5" r="0.5">
      <stop offset="0" style="stop-color:var(--blood-bright)" stop-opacity="0.85"/>
      <stop offset="0.6" style="stop-color:var(--blood-deep)" stop-opacity="0.8"/>
      <stop offset="1" style="stop-color:var(--blood-deep)" stop-opacity="0"/>
    </radialGradient>
    <linearGradient id="titleGloss" x1="0" y1="0" x2="0" y2="1">
      <stop offset="0" style="stop-color:var(--title-light)"/>
      <stop offset="0.45" style="stop-color:var(--title-dark)"/>
      <stop offset="1" style="stop-color:var(--title-light)"/>
    </linearGradient>
  </defs>

  <!-- Front cover -->
  <g class="front-cover">
    <rect class="front-board" x="188" y="115" width="420" height="645" style="fill:url(#coverFill)"/>
    <text class="title-verb" x="228" y="328" font-size="230" textLength="114" lengthAdjust="spacingAndGlyphs">Win</text>
    <text class="title-word" x="380" y="295" font-size="120" textLength="150" lengthAdjust="spacingAndGlyphs">The</text>
    <rect class="cover-illustration" x="265" y="335" width="260" height="265"
          style="fill:url(#splatterFill)" role="img"
          aria-label="Red splatter illustration with a microphone and interview desk"/>
    <text class="title-word" x="200" y="745" font-size="120" textLength="400" lengthAdjust="spacingAndGlyphs">Hiring Room</text>
  </g>

  <!-- Spine -->
  <g class="spine">
    <rect class="spine-board" x="787" y="40" width="180" height="905" style="fill:url(#spineFill)"/>
    <text class="title-verb title-verb--spine" transform="translate(808 215) rotate(90)" font-size="215" textLength="66" lengthAdjust="spacingAndGlyphs">Win</text>
    <text class="title-word" transform="translate(833 370) rotate(90)" font-size="110" textLength="95" lengthAdjust="spacingAndGlyphs">The</text>
    <text class="title-word" transform="translate(833 555) rotate(90)" font-size="110" textLength="255" lengthAdjust="spacingAndGlyphs">Hiring Room</text>
  </g>
</svg>
</body>
</html>
```